International IT Business Needs a Proffesional and Innovative Business Card

We need a proffesional and innovative business card for a new company based in Venezuela called 'QuillonMark'. We are RVK Business Partner, RVK is a key manufacture for us, one of the most influential players in technology, and the leader in cloud computing, virtualization, Big Data storage and analytics, and IT security and protection.

RVK has developed a global network of business partners to bring customers the full complement of skills and expertise required to build their information infrastructures. This partner ecosystem helps customers maximize the value of their information at the lowest total cost.

We would like to see designs that use the RVK Business Partnet logo & QuillonMark logo.

http://brand.rvk-example.com/BrandGuide/partners/rvk-business-partner-logo/

Thank you in advance for your interest.

Happy Day!!!! I look forward to your creative design!!!

Thank you in advance.

Marisol Quevedo

Target Market(s)

QuillonMark's target markets include large companies and small- and medium-sized businesses across various vertical markets.

Industry/Entity Type

Security

Font styles to use
Other font styles liked:
• We use Meta as the RVK® corporate font.

Colors

Designer to choose colors to be used in the design.

Requirements
Must have
• Name
Title
Address
web page (www.quillon-example.la)

Nice to have
• Add a QR code on the reverse of the card.

```html
<!DOCTYPE html>
<html lang="en">
<head>
<meta charset="utf-8">
<title>QuillonMark Business Cards</title>
<link rel="stylesheet" href="https://fonts.googleapis.com/css2?family=Exo+2:wght@300;400;600&display=swap">
<style>
  :root {
    --navy: #18327a;
    --navy-deep: #0f2563;
    --blue-bright: #2f5fd0;
    --green: #25a244;
    --panel: #eef0f3;
    --panel-shade: #d9dde3;
    --white: #ffffff;
    --ink: #2b2f38;
    --bg: #e9e6e1;
  }
  * { box-sizing: border-box; margin: 0; padding: 0; }
  html, body { width: 1200px; height: 970px; overflow: hidden; background: var(--bg); }
  body { font-family: "Exo 2", sans-serif; position: relative; }

  .card {
    position: absolute;
    left: 220px;
    width: 760px;
    height: 434px;
    box-shadow: 0 6px 18px rgba(0,0,0,0.18);
    overflow: hidden;
  }
  .card--front { top: 36px; background: var(--navy); }
  .card--back { top: 500px; background: var(--green); }
  .card svg.shapes { position: absolute; inset: 0; }

  .logo {
    position: absolute;
    display: flex;
    align-items: center;
    gap: 10px;
    font-family: "Exo 2", sans-serif;
    font-weight: 600;
    font-size: 40px;
    color: var(--navy);
    letter-spacing: 0.5px;
  }
  .logo__dot {
    width: 22px; height: 22px;
    border-radius: 50%;
    background: var(--green);
  }
  .card--front .logo { left: 70px; top: 120px; }
  .card--back .logo { left: 470px; top: 232px; font-size: 36px; }

  .website {
    position: absolute;
    left: 60px; bottom: 22px;
    color: var(--white);
    font-size: 15px;
    font-weight: 400;
    letter-spacing: 0.4px;
  }

  .address {
    position: absolute;
    left: 34px; top: 30px;
    color: var(--white);
    font-size: 18px;
    font-weight: 400;
    letter-spacing: 0.6px;
  }
  .person {
    position: absolute;
    left: 40px; top: 102px;
    color: var(--ink);
    text-transform: uppercase;
  }
  .person__name { font-size: 28px; font-weight: 400; letter-spacing: 1.5px; line-height: 1.1; }
  .person__title { font-size: 19px; font-weight: 300; letter-spacing: 1.4px; margin-top: 4px; }

  .contacts {
    position: absolute;
    left: 40px; top: 250px;
    list-style: none;
    color: var(--white);
    font-size: 15px;
    font-weight: 400;
    letter-spacing: 0.4px;
  }
  .contacts li { display: flex; align-items: center; gap: 12px; height: 28px; }
  .contacts svg { width: 15px; height: 15px; fill: var(--white); flex: none; }
</style>
</head>
<body>

<section class="card card--front" aria-label="Card front">
  <svg class="shapes" width="760" height="434" viewBox="0 0 760 434">
    <defs>
      <linearGradient id="stripe" x1="0" y1="0" x2="1" y2="1">
        <stop offset="0" stop-color="#1a3a9a"/>
        <stop offset="0.5" stop-color="#3a76e0"/>
        <stop offset="1" stop-color="#1a3a9a"/>
      </linearGradient>
      <linearGradient id="mapTone" x1="0" y1="0" x2="1" y2="0">
        <stop offset="0" stop-color="#d3d7dd"/>
        <stop offset="1" stop-color="#eceef1"/>
      </linearGradient>
    </defs>
    <path d="M30 24 H730 V360 H100 L86 346 L72 360 H30 Z" fill="var(--panel)"/>
    <rect x="30" y="24" width="470" height="300" fill="url(#mapTone)" opacity="0.7" role="img" aria-label="Faint world map backdrop"/>
    <path d="M560 24 H730 V160 L600 300 H430 Z" fill="url(#stripe)"/>
  </svg>
  <div class="logo"><span class="logo__dot"></span>QuillonMark</div>
  <p class="website">www.quillon-example.la</p>
</section>

<section class="card card--back" aria-label="Card back">
  <svg class="shapes" width="760" height="434" viewBox="0 0 760 434">
    <defs>
      <linearGradient id="nameBox" x1="0" y1="0" x2="1" y2="0">
        <stop offset="0" stop-color="#ffffff"/>
        <stop offset="1" stop-color="#d6d9de"/>
      </linearGradient>
    </defs>
    <rect x="16" y="16" width="400" height="60" fill="var(--navy)"/>
    <rect x="16" y="76" width="400" height="140" fill="url(#nameBox)"/>
    <rect x="16" y="216" width="400" height="202" fill="var(--navy)"/>
    <path d="M430 110 H744 V418 H430 V160 L444 146 L430 132 Z" fill="var(--panel)"/>
  </svg>

  <p class="address">42 Avenida Norte, Torre B, Piso 3</p>

  <div class="person">
    <p class="person__name">Tomas Revelo</p>
    <p class="person__title">General Manager</p>
  </div>

  <ul class="contacts">
    <li><svg viewBox="0 0 16 16"><path d="M3 1 L6 1 L7 5 L5 6 C6 8 8 10 10 11 L11 9 L15 10 L15 13 C15 14 14 15 13 15 C6 15 1 10 1 3 C1 2 2 1 3 1 Z"/></svg>012 555 0187</li>
    <li><svg viewBox="0 0 16 16"><path d="M4 0 H12 V16 H4 Z M5 2 V13 H11 V2 Z"/></svg>012 555 0187</li>
    <li><svg viewBox="0 0 16 16"><path d="M4 0 H12 V5 H15 V12 H12 V16 H4 V12 H1 V5 H4 Z M5 1 V5 H11 V1 Z M5 10 V15 H11 V10 Z"/></svg>012 555 0187</li>
    <li><svg viewBox="0 0 16 16"><path d="M1 3 H15 V13 H1 Z M2 4 L8 9 L14 4 Z"/></svg>contact@quillon-example.la</li>
    <li><svg viewBox="0 0 16 16"><path d="M8 0 A8 8 0 1 0 8 16 A8 8 0 1 0 8 0 Z M8 1.5 A6.5 6.5 0 1 1 8 14.5 A6.5 6.5 0 1 1 8 1.5 Z M1.5 7.3 H14.5 V8.7 H1.5 Z M7.3 1.5 H8.7 V14.5 H7.3 Z"/></svg>www.quillon-example.la</li>
  </ul>

  <div class="logo"><span class="logo__dot"></span>QuillonMark</div>
</section>

</body>
</html>
```